Lantern Pantry cafe promotion flyer

Lantern Pantry is a waterfront cafe/ function center with gorgeous views. Lantern Pantry is a very modern venue that can cater for 200 people (seating) and it is located in a business area.

The main customers are the professional bank employees (80%) with the remaining being other corporate workers. Lantern Pantrys main trading periods are Morning Coffee, Breakfast and Lunch with the average spend being between $5-$15 per head. Hospitality is a highly competitive market and since there is not much general foot traffic on the waterfront side during winter, Lantern Pantry have decided to advertise by sending out some flyers to all the nearby buildings, to let the Quayside Neighbourhood know where we are, what we offer and to generate new business.

We would like to design a unique flyer with a great title, plus the deals we offer, plus some pictures , would prefer fresh and bright colour which can attract people from outside the venue .You can visit our website and have a look at our venue to get some idea as well:
www.thelanternpantry.com.au

Thanks for the designs submitted so far.
but I prefer the background color is bight color, like fresh food color will be better, prefer orange, green, yellow that kind of fresh color, can entice people to come in and have their lunch or breakfast.

I would prefer to have a picture of coffee with coffee art, food change to a big sandwich or burger. The entire flyer is try to entice the customer to come in eat and drink. The flyer is going to be put on a black board, so there should be some contrast in the colour.

look forward to your new design.

Here is a sample title:
only our special offers warm up your savings

(or something similar, more creative and appealing to the potential customers)

Monday-Friday, early bird coffee 7:30a-8:30am, small for $2.80, large for $3.30.

Deals detail:
coffee with freshly home-made muffin $5.50
Coffee with egg bacon muffin $6.90
Coffee with gourmet egg bacon wrap $8.50
Coffee with fruit toast $6.50

Lunch Special:
Only $4 for a glass of wine/a bottle of beer with our daily Lunch specail
Buy any Focaccia for only $8.90 get one soft drink free

Friday Happy hour drinks 12pm-7pm,
selection of wine/beer/spirits for only $6

corporate catering and function room hire available
Waterfront Side, QVR building, 412 Wexley Street, Docklands 3008
E:catering@thelanternpantry.com.au
P:03 9481 2257

we require hi resolution PDF files of both A5 and A3 Poster

                                       

Hi all designers

but I prefer the background color  is bight color, like fresh food color will be better, prefer orange, green, yellow that kind of fresh color, can entice people to come in and have their lunch or breakfast.

I would prefer to change the coffee to a coffee with coffee art, food change to a better sandwich or burger or focaccia. The entire flyer is try to entice the customer to come in eat and drink.

will you be able to add this to it:

Also, can you please take away the live band 4p-7pm for Fridays , thanks.

Target Market(s)

the target customers are the corporates who has something quick to eat for breakfast and lunch, normally on a budget.

Industry/Entity Type

Catering

Requirements
Must have
• great food and drink pictures
Should not have
• dark colour

```html
<!DOCTYPE html>
<html lang="en">
<head>
<meta charset="utf-8">
<title>Lantern Pantry – Special Offers</title>
<link rel="stylesheet" href="https://fonts.googleapis.com/css2?family=Cabin+Sketch:wght@400;700&family=Short+Stack&display=swap">
<style>
  :root {
    --panel-top: #f5962a;
    --panel-bottom: #e4671a;
    --chalk: #ffffff;
    --accent-red: #a10d07;
    --brand-lime: #c8d44a;
    --fire-core: #ffb22e;
    --fire-mid: #e0561a;
    --hero-edge: #7a2a0c;
    --dot: #ffffff;
    --shade: rgba(80, 25, 0, .35);
  }
  * { box-sizing: border-box; margin: 0; padding: 0; }
  html, body { width: 848px; height: 1200px; overflow: hidden; background: var(--panel-bottom); }
  .flyer {
    position: relative; width: 848px; height: 1200px; overflow: hidden;
    background: linear-gradient(to bottom, var(--panel-top) 0%, var(--panel-bottom) 100%);
    color: var(--chalk);
    font-family: "Short Stack", "Comic Sans MS", cursive;
    text-shadow: 0 2px 0 var(--shade);
  }
  .flyer > * { position: absolute; }
  .display { font-family: "Cabin Sketch", "Comic Sans MS", cursive; }

  .hero-photo {
    left: 0; top: 0; width: 848px; height: 570px;
    background:
      radial-gradient(ellipse 240px 170px at 400px 320px, var(--fire-core) 0%, #f47a16 40%, var(--fire-mid) 70%, transparent 100%),
      radial-gradient(ellipse 460px 380px at 420px 290px, #a8380e 0%, var(--hero-edge) 65%, #5a1e08 100%);
  }
  .hero-fade {
    left: 0; top: 400px; width: 848px; height: 170px;
    background: linear-gradient(to bottom, transparent, var(--panel-top));
  }
  .brand-name {
    left: 0; width: 848px; top: 108px; text-align: center;
    font-size: 36px; font-weight: 400; letter-spacing: 2px; color: var(--brand-lime);
    text-shadow: none;
  }
  .headline {
    left: 0; width: 848px; top: 408px; text-align: center;
    font-size: 58px; font-weight: 700; line-height: 64px; letter-spacing: 1px;
  }

  .dots {
    height: 8px;
    background-image: radial-gradient(circle at 4px 4px, var(--dot) 3px, transparent 3.4px);
    background-size: 9px 8px;
  }
  .dots.full { left: 30px; width: 788px; }
  .dots.half { left: 30px; width: 545px; }

  .coffee-photo {
    left: 40px; top: 562px; width: 135px; height: 122px; border-radius: 50%;
    background: radial-gradient(ellipse at 50% 40%, #3a1f12 0 22%, #f4f4f4 24% 62%, #d8d8d8 80%, transparent 82%);
  }
  .combo-list { left: 200px; top: 565px; width: 608px; list-style: none; font-size: 22px; line-height: 28.5px; }
  .combo-list li { display: flex; justify-content: space-between; }

  .lunch-title { left: 32px; top: 712px; font-size: 54px; font-weight: 700; color: var(--accent-red); line-height: 60px; text-shadow: none; }
  .only-tag { left: 28px; top: 846px; font-size: 22px; line-height: 24px; transform: rotate(-90deg); transform-origin: left top; }
  .lunch-price { left: 66px; top: 772px; font-size: 56px; font-weight: 700; line-height: 66px; }
  .lunch-copy { left: 185px; top: 776px; font-size: 17.5px; line-height: 23px; }
  .drinks-photo {
    left: 432px; top: 720px; width: 135px; height: 128px; border-radius: 10px;
    background: linear-gradient(160deg, #8a2a10 0%, #d9651e 40%, #e9d6b8 70%, #6a5e5a 100%);
  }

  .focaccia-title { left: 588px; top: 712px; width: 220px; text-align: center; line-height: 52px; }
  .focaccia-title .big { display: block; font-size: 48px; }
  .focaccia-title .name { display: block; font-size: 38px; line-height: 46px; }
  .focaccia-photo {
    left: 585px; top: 835px; width: 218px; height: 125px; border-radius: 14px;
    background: linear-gradient(170deg, #f2dcc0 0%, #d49a60 45%, #a8693a 75%, #7a4722 100%);
  }

  .happy-kicker { left: 35px; top: 880px; font-size: 15px; }
  .happy-title { left: 34px; top: 900px; font-size: 56px; font-weight: 700; line-height: 58px; color: var(--accent-red); text-shadow: none; }
  .happy-copy { left: 222px; top: 888px; }
  .happy-copy .lg { font-size: 29px; line-height: 40px; display: block; }
  .happy-copy .sm { font-size: 19px; line-height: 32px; display: block; }

  .group-label { left: 37px; top: 1044px; font-size: 26px; line-height: 32px; }
  .group-size { left: 194px; top: 1034px; font-size: 64px; font-weight: 700; line-height: 74px; color: var(--accent-red); text-shadow: none; }
  .group-copy { left: 282px; top: 1046px; font-size: 15px; }
  .group-discount { left: 340px; top: 1068px; font-size: 30px; font-weight: 700; color: var(--accent-red); text-shadow: none; }

  .focaccia-deal { left: 588px; top: 990px; }
  .focaccia-deal .lead { display: block; font-size: 30px; line-height: 34px; }
  .focaccia-deal .price { display: block; font-size: 58px; font-weight: 700; line-height: 60px; }
  .focaccia-deal .note { display: block; font-size: 17px; line-height: 22px; }

  .address { left: 0; width: 848px; top: 1140px; text-align: center; font-size: 16.5px; }
</style>
</head>
<body>
<main class="flyer">
  <div class="hero-photo" role="img" aria-label="Photo of a wood-fired oven with a roaring log fire"></div>
  <div class="hero-fade"></div>
  <div class="brand-name display">LANTERN PANTRY</div>
  <h1 class="headline display">ONLY OUR SPECIAL OFFERS,<br>WARM UP YOUR SAVINGS!</h1>

  <div class="dots full" style="top:544px"></div>
  <div class="coffee-photo" role="img" aria-label="Photo of a white cup of coffee on a saucer"></div>
  <ul class="combo-list">
    <li><span>Coffee with fresh home-made muffin</span><span>$ 5. 50</span></li>
    <li><span>Coffee with egg bacon muffin</span><span>$ 6. 90</span></li>
    <li><span>Coffee with gourmet egg bacon wrap</span><span>$ 8. 50</span></li>
    <li><span>Coffee with fruit toast</span><span>$ 6. 50</span></li>
  </ul>

  <div class="dots full" style="top:696px"></div>
  <h2 class="lunch-title display">LUNCH SPECIAL</h2>
  <span class="only-tag">only</span>
  <span class="lunch-price">$ 4</span>
  <p class="lunch-copy">for a glass of wine /<br>a bottle or beer with<br>our daily lunch special</p>
  <div class="drinks-photo" role="img" aria-label="Photo of a glass of beer, a latte and a glass of wine"></div>

  <h2 class="focaccia-title"><span class="big">Buy any</span><span class="name">FOCACCIA</span></h2>
  <div class="focaccia-photo" role="img" aria-label="Photo of focaccia squares on a wooden board"></div>

  <div class="dots half" style="top:861px"></div>
  <span class="happy-kicker">FRIDAY AFTERNOON</span>
  <h2 class="happy-title display">HAPPY<br>HOUR</h2>
  <p class="happy-copy">
    <span class="lg">drink 12 PM - 7 PM</span>
    <span class="sm">selection of wine / beer / spirits</span>
    <span class="lg">for only $ 6</span>
  </p>

  <div class="focaccia-deal">
    <span class="lead">for only</span>
    <span class="price">$ 8. 90</span>
    <span class="note">get one soft drink free</span>
  </div>

  <div class="dots half" style="top:1024px"></div>
  <p class="group-label">Any group<br>booking</p>
  <span class="group-size display">8+</span>
  <p class="group-copy">for breakfast / lunch will get</p>
  <span class="group-discount display">10% DISCOUNT</span>

  <div class="dots full" style="top:1122px"></div>
  <p class="address">412 Wexley Street, Quayside Harbour, Docklands Melbourne &nbsp;- &nbsp;TEL +613 9481 2257</p>
</main>
</body>
</html>
```